Harold The Realtor Business Card Design

I need a new card design for my real estate business in Seattle Wa. I am interested in a unique design. My business revolves around my personal services and I want the card to show professionalism, creativity and good execution. I specialize in residential real estate in Maple ridge / downtown neighborhoods. The card is my first impression on may of my clients and in the service industry any time you can stand out from the crowd and make an impression will go a long way.

Target Market(s)

I will be handing the card to prospects/ potential buyers and sellers of residential real estate.

Industry/Entity Type

Real Estate Agent

Contact Information for Business Card

Email: Info@Haroldtherealtor.com Website: HaroldtheRealtor.com Cell phone: 206-555-0184 Fax 206-555-0127

Font styles to use
Sans Serif

Colors
0255a3
ffc214

Requirements
Must have
• I will need to have my firms logo "Keystone 8" and my logo "HTR" on the business card. I would like to have my firms logo smaller then mine. I would also like to have my photo on the card. By business colors are gold and white with blue accents.
Nice to have
• It would be nice to have a unique shape or feel (texture) rather then your standard business card. I saw cardly press had metal cards which could be interesting.

```html
<!DOCTYPE html>
<html lang="en">
<head>
<meta charset="utf-8">
<title>Harold The Realtor – Business Card</title>
<link rel="stylesheet" href="https://fonts.googleapis.com/css2?family=Lato:wght@400;700&display=swap">
<style>
  :root {
    --gold: #8c7231;
    --gold-dark: #7a5e22;
    --white: #ffffff;
    --ink: #2b2b2b;
    --page: #e9e7e2;
    --photo-top: #2f3b52;
    --photo-mid: #5a4538;
    --photo-low: #3b4a66;
  }
  * { margin: 0; padding: 0; box-sizing: border-box; }
  html, body { width: 1200px; height: 900px; overflow: hidden; }
  body {
    background: var(--page);
    font-family: "Lato", sans-serif;
    position: relative;
  }
  .card {
    position: absolute;
    left: 285px;
    width: 630px;
    height: 360px;
    overflow: hidden;
    box-shadow: 0 6px 18px rgba(0,0,0,.18);
  }
  /* ---------- back side ---------- */
  .card-back { top: 50px; background: var(--white); }
  .card-back .band { position: absolute; left: 0; width: 100%; background: var(--gold); }
  .card-back .band-top { top: 0; height: 40px; }
  .card-back .band-bottom { bottom: 0; height: 44px; }
  .firm-name {
    position: absolute;
    top: 66px;
    right: 38px;
    font-weight: 400;
    font-size: 24px;
    color: var(--ink);
  }
  .contact-list {
    position: absolute;
    left: 34px;
    bottom: 66px;
    list-style: none;
    font-size: 14px;
    color: var(--ink);
  }
  .contact-list li {
    display: flex;
    align-items: center;
    gap: 10px;
    line-height: 22px;
  }
  .contact-list svg { width: 14px; height: 14px; fill: var(--gold); flex: none; }
  /* ---------- front side ---------- */
  .card-front { top: 470px; }
  .card-front svg.layout { position: absolute; inset: 0; width: 100%; height: 100%; }
  .agent-name {
    position: absolute;
    left: 222px;
    top: 158px;
    color: var(--gold-dark);
    font-weight: 700;
  }
  .agent-name .name { font-size: 44px; line-height: 1; display: block; }
  .agent-name .title { font-size: 13px; letter-spacing: 3px; display: block; margin-top: 6px; padding-left: 2px; }
</style>
</head>
<body>

<section class="card card-back" aria-label="Business card back">
  <div class="band band-top"></div>
  <div class="band band-bottom"></div>
  <div class="firm-name">Keystone 8</div>
  <ul class="contact-list">
    <li><svg viewBox="0 0 16 16"><path d="M3 2h3l1 4-2 1a9 9 0 0 0 4 4l1-2 4 1v3c0 1-1 1-1 1C7 14 2 9 2 3c0 0 0-1 1-1z"/></svg>206-555-0184</li>
    <li><svg viewBox="0 0 16 16"><path d="M4 1h8v4H4zM1 6h14v6h-3v3H4v-3H1zM5 10v4h6v-4z"/></svg>206-555-0127</li>
    <li><svg viewBox="0 0 16 16"><path d="M1 3h14v10H1zM2 4l6 5 6-5v-.5H2z" fill-rule="evenodd"/></svg>Info@Haroldtherealtor.com</li>
    <li><svg viewBox="0 0 16 16"><circle cx="8" cy="8" r="6.5" fill="none" stroke="var(--gold)" stroke-width="1.5"/><path d="M1.5 8h13M8 1.5v13" stroke="var(--gold)" stroke-width="1.2" fill="none"/></svg>HaroldtheRealtor.com</li>
  </ul>
</section>

<section class="card card-front" aria-label="Business card front">
  <svg class="layout" viewBox="0 0 630 360" preserveAspectRatio="none">
    <defs>
      <linearGradient id="portrait-tone" x1="0" y1="0" x2="0" y2="1">
        <stop offset="0" stop-color="var(--photo-mid)"/>
        <stop offset=".45" stop-color="var(--photo-top)"/>
        <stop offset="1" stop-color="var(--photo-low)"/>
      </linearGradient>
    </defs>
    <rect class="card-ground" width="630" height="360" fill="var(--gold)"/>
    <polygon class="white-band" points="150,110 630,110 630,290 150,290 190,200" fill="var(--white)"/>
    <polygon class="chevron" points="40,150 70,150 110,205 80,255 50,255 80,205" fill="var(--white)"/>
    <polygon class="chevron" points="90,130 120,130 165,205 130,270 100,270 135,205" fill="var(--white)"/>
    <path role="img" aria-label="Portrait photo of the agent in a navy suit" d="M400 40 H630 V300 H430 Q400 300 400 270 Z" fill="url(#portrait-tone)"/>
  </svg>
  <div class="agent-name">
    <span class="name">Harold</span>
    <span class="title">THE REALTOR</span>
  </div>
</section>

</body>
</html>
```